T & M Oriental Pantry needs a logo design

We need abusiness card design that depicts our business based in Australia servicing 90% of the Filipino Community.. We send door-to door balikbayan boxes / money transfers to the philippines...we sell/ retail Filipino Groceries...

Target Market(s)

adults / couples - Aussie / Filipino community

Industry/Entity Type

Retail

Font styles to use
Sans Serif

Requirements
Must have
• must have the KW Courier design on the other side (for the Money Transfer & door to door services to the philippines) but just to change the contact number to - 0412 574 302 and include the area of coverage which is - Coffs Harbour

on the other side you can design whatever would be in mind depicting the retail store
Nice to have
• the attached files are the previous calling cards/ signage that I made thru Lumo press & mark o dome

a logo that is attractive to the one who would look at it

```html
<!DOCTYPE html>
<html lang="en">
<head>
<meta charset="UTF-8">
<title>T &amp; M Oriental Pantry – Business Card</title>
<link rel="stylesheet" href="https://fonts.googleapis.com/css2?family=Arimo:wght@400&display=swap">
<style>
  :root {
    --paper: #ffffff;
    --plum: #8a0a5e;
    --plum-soft: #ecd0e2;
    --forest: #2f5e31;
    --leaf: #2c9a2c;
    --on-plum: #ffffff;
  }
  html, body {
    margin: 0;
    padding: 0;
    width: 1200px;
    height: 686px;
    overflow: hidden;
    background: var(--paper);
  }
  .card {
    position: relative;
    width: 1200px;
    height: 686px;
    background: var(--paper);
    font-family: "Arimo", Arial, sans-serif;
    overflow: hidden;
  }
  .brand {
    position: absolute;
    left: 40px;
    top: 30px;
    width: 440px;
    margin: 0;
    display: flex;
    flex-direction: column;
    align-items: center;
  }
  .brand-mark {
    width: 240px;
    height: 240px;
    border-radius: 50%;
    background: var(--plum-soft);
  }
  .brand-name {
    margin-top: 44px;
    color: var(--leaf);
    font-size: 38px;
    font-weight: 400;
    line-height: 1;
    white-space: nowrap;
  }
  .person-name {
    position: absolute;
    right: 28px;
    top: 362px;
    margin: 0;
    color: var(--forest);
    font-size: 84px;
    font-weight: 400;
    line-height: 1;
    white-space: nowrap;
  }
  .rule {
    position: absolute;
    left: 0;
    top: 470px;
    width: 1200px;
    height: 8px;
    background: var(--plum);
  }
  .contact-band {
    position: absolute;
    left: 0;
    top: 491px;
    width: 1200px;
    height: 195px;
    background: var(--plum);
    color: var(--on-plum);
  }
  .address {
    position: absolute;
    left: 34px;
    top: 52px;
    margin: 0;
    font-style: normal;
    font-size: 38px;
    line-height: 55px;
    white-space: nowrap;
  }
  .divider {
    position: absolute;
    left: 616px;
    top: 30px;
    width: 3px;
    height: 152px;
    background: var(--on-plum);
  }
  .contact-list {
    position: absolute;
    left: 643px;
    top: 26px;
    margin: 0;
    padding: 0;
    list-style: none;
    font-size: 34px;
    line-height: 49px;
    white-space: nowrap;
  }
</style>
</head>
<body>
  <main class="card">
    <h1 class="brand">
      <span class="brand-mark"></span>
      <span class="brand-name">T &amp; M Oriental Pantry</span>
    </h1>
    <p class="person-name">Lorna Dizon</p>
    <div class="rule"></div>
    <section class="contact-band">
      <address class="address">14 Harbour View Road<br>Sawtell Heights, NSW 2456</address>
      <div class="divider"></div>
      <ul class="contact-list">
        <li>Phone: (02) 6651 4920</li>
        <li>Mobile: 0412 574 302</li>
        <li>Email: ldizon@mailbox.com</li>
      </ul>
    </section>
  </main>
</body>
</html>
```